Expense Tracker App for Young Adults

I need a mobile app designer to design an app UI for me. It is for an expense tracker app. I’ve attached a mind map of the various screens and features of the app.

I would like to see designs for this app which is targeted towards young adults (late teens & early 20s) just starting their career who want to plan their budgets and track their expenses.
Updates

Hello designers! I'm conscious that this is not a guaranteed project, so I can understand that some of you might be apprehensive. Just wanted to let you know that I'm willing to see your initial drafts that show your direction and theme for design. You don't have to design the whole app. In fact, it's better if you share your initial design ideas so that we can have a discussion and I can give my input. If I see some good initial designs, I will be happy to make this a guaranteed project. I'm simply being cautious since I'm bootstrapping this and funding out of my own pocket. Thank you for your understanding!

Target Market(s)

Young adults who are just starting their careers, late teens and early 20s.

Font styles to use
Sans Serif

Requirements
Must have
• Ease of use, smart and sleek, a guided setup wizard which will help users setup their account after signing up.
Should not have
• Clunky

```html
<!DOCTYPE html>
<html lang="en">
<head>
<meta charset="utf-8">
<title>Expense Tracker – Home</title>
<link href="https://fonts.googleapis.com/css2?family=Rubik:wght@400;500;600;700;800&display=swap" rel="stylesheet">
<style>
:root{
  --plum:#44214A;
  --plum-faded:#6C5475;
  --plum-muted:#5B4063;
  --bar:#523A5E;
  --bar-orange:#EE8867;
  --bar-yellow:#EFB04B;
  --teal:#22BDB0;
  --white:#FFFFFF;
  --ink:#1F2227;
  --grey:#A6A6A6;
  --nav-grey:#9B9B9B;
  --nav-active:#74307F;
  --line:#F0F0F2;
}
*{margin:0;padding:0;box-sizing:border-box}
html,body{width:1200px;height:2598px;overflow:hidden;background:var(--white)}
body{font-family:'Rubik',sans-serif}
.screen{position:absolute;left:0;top:0;width:1190px;height:2576px;transform:scale(1.0084);transform-origin:0 0;background:var(--plum);overflow:hidden}
.abs{position:absolute;line-height:1.2;white-space:nowrap}
.status-time{left:105px;top:49px;font-size:40px;color:var(--white);font-weight:400}
.status-icons{left:920px;top:50px}
.year{left:475px;top:160px;display:flex;align-items:center;gap:48px;color:var(--plum-faded);font-size:44px;font-weight:700}
.month{top:288px;font-size:58px;font-weight:700}
.month-prev{left:30px;color:var(--plum-muted)}
.month-current{left:0;width:1190px;text-align:center;color:var(--white)}
.month-next{left:960px;color:var(--plum-muted)}
.sheet{position:absolute;left:0;top:428px;width:1190px;height:2200px;background:var(--white);border-radius:90px 90px 0 0}
.summary-card{position:absolute;left:95px;top:543px;width:1000px;height:690px;background:var(--plum);border-radius:75px}
.summary-label{left:65px;top:78px;font-size:36px;color:var(--white)}
.summary-total{left:63px;top:146px;font-size:76px;font-weight:800;color:var(--white)}
.summary-change{left:710px;top:118px;font-size:54px;font-weight:700;color:var(--teal)}
.summary-arrow{left:876px;top:135px}
.bar{position:absolute;width:50px;bottom:76px;border-radius:25px;background:var(--bar)}
.bar.low{background:var(--bar-orange)}
.bar.high{background:var(--bar-yellow)}
.section-title{left:96px;top:1284px;font-size:42px;font-weight:700;color:var(--ink)}
.day{font-size:42px;font-weight:500;color:var(--ink)}
.row-label{font-size:36px;font-weight:500;color:var(--grey)}
.row-amount{font-size:36px;font-weight:500;color:var(--ink);text-align:right;width:300px}
.divider{position:absolute;height:3px;width:1000px;background:var(--line)}
.nav{position:absolute;left:0;top:2378px;width:1190px;height:200px;background:var(--white);border-top:2px solid var(--line)}
.fab-ring{position:absolute;left:490px;top:2271px;width:214px;height:214px;border-radius:50%;background:var(--white);border:2px solid var(--line)}
.fab{position:absolute;left:505px;top:2286px;width:184px;height:184px;border-radius:50%;background:var(--teal);display:flex;align-items:center;justify-content:center}
.nav-item{position:absolute;top:2410px;width:200px;display:flex;flex-direction:column;align-items:center;gap:18px;font-size:36px;font-weight:500;color:var(--nav-grey)}
.nav-item.active{color:var(--nav-active)}
</style>
</head>
<body>
<div class="screen">
  <div class="abs status-time">9:41</div>
  <svg class="abs status-icons" width="215" height="40" viewBox="0 0 215 40">
    <g fill="#fff">
      <rect x="2" y="26" width="9" height="10" rx="2"/><rect x="16" y="19" width="9" height="17" rx="2"/>
      <rect x="30" y="12" width="9" height="24" rx="2"/><rect x="44" y="4" width="9" height="32" rx="2"/>
    </g>
    <path d="M73 14a34 34 0 0 1 46 0M80 21a24 24 0 0 1 32 0M87 28a13 13 0 0 1 18 0" stroke="#fff" stroke-width="6" fill="none" stroke-linecap="round"/>
    <circle cx="96" cy="34" r="4" fill="#fff"/>
    <rect x="139" y="3" width="68" height="33" rx="9" stroke="#fff" stroke-width="4" fill="none"/>
    <rect x="145" y="9" width="56" height="21" rx="5" fill="#fff"/>
    <rect x="210" y="14" width="4" height="11" rx="2" fill="#fff"/>
  </svg>

  <div class="abs year">
    <svg width="44" height="48" viewBox="0 0 44 48" fill="none" stroke="var(--plum-faded)" stroke-width="4" stroke-linecap="round">
      <rect x="3" y="8" width="38" height="37" rx="6"/><path d="M3 19h38M13 3v9M31 3v9M12 28h4M22 28h4M12 36h14"/>
    </svg>
    <span>2020</span>
  </div>
  <div class="abs month month-prev">August</div>
  <div class="abs month month-current">September</div>
  <div class="abs month month-next">November</div>

  <div class="sheet"></div>

  <section class="summary-card">
    <div class="abs summary-label">Total Expenses (This Month)</div>
    <div class="abs summary-total">4,500 $</div>
    <div class="abs summary-change">65%</div>
    <svg class="abs summary-arrow" width="48" height="30" viewBox="0 0 48 30"><path d="M4 25L24 7l20 18" stroke="var(--teal)" stroke-width="6" fill="none" stroke-linecap="round"/></svg>
    <div class="bar" style="left:64px;height:187px"></div>
    <div class="bar" style="left:140px;height:110px"></div>
    <div class="bar" style="left:216px;height:187px"></div>
    <div class="bar" style="left:293px;height:161px"></div>
    <div class="bar low" style="left:369px;height:59px"></div>
    <div class="bar high" style="left:445px;height:234px"></div>
    <div class="bar" style="left:521px;height:187px"></div>
    <div class="bar" style="left:600px;height:161px"></div>
    <div class="bar" style="left:676px;height:94px"></div>
    <div class="bar" style="left:752px;height:187px"></div>
    <div class="bar" style="left:832px;height:161px"></div>
    <div class="bar" style="left:908px;height:94px"></div>
  </section>

  <div class="abs section-title">Latest Expenses</div>

  <div class="abs day" style="left:96px;top:1421px">Today</div>
  <div class="abs row-label" style="left:96px;top:1551px">Rent</div>
  <div class="abs row-amount" style="left:795px;top:1551px">250 $</div>
  <div class="abs row-label" style="left:96px;top:1646px">Food</div>
  <div class="abs row-amount" style="left:795px;top:1646px">10 $</div>
  <div class="divider" style="left:96px;top:1740px"></div>

  <div class="abs day" style="left:99px;top:1792px">Yesterday</div>
  <div class="abs row-label" style="left:99px;top:1922px">Rent</div>
  <div class="abs row-amount" style="left:798px;top:1922px">250 $</div>
  <div class="abs row-label" style="left:99px;top:2017px">Food</div>
  <div class="abs row-amount" style="left:798px;top:2017px">10 $</div>
  <div class="divider" style="left:99px;top:2100px"></div>

  <nav class="nav"></nav>
  <div class="fab-ring"></div>
  <div class="fab">
    <svg width="56" height="56" viewBox="0 0 56 56"><path d="M28 4v48M4 28h48" stroke="#fff" stroke-width="6" stroke-linecap="round"/></svg>
  </div>

  <div class="nav-item active" style="left:20px">
    <svg width="68" height="68" viewBox="0 0 68 68" fill="none" stroke="var(--nav-active)" stroke-width="6" stroke-linejoin="round">
      <path d="M28 10a26 26 0 1 0 30 30H28z"/><path d="M37 4a28 28 0 0 1 27 27H37z"/>
    </svg>
    <span>Home</span>
  </div>
  <div class="nav-item" style="left:258px">
    <svg width="68" height="68" viewBox="0 0 68 68" fill="none" stroke="var(--nav-grey)" stroke-width="6" stroke-linejoin="round" stroke-linecap="round">
      <path d="M12 6h28l16 16v40H12z"/><path d="M40 6v16h16M24 38h20M24 48h14"/>
    </svg>
    <span>Reports</span>
  </div>
  <div class="nav-item" style="left:736px">
    <svg width="68" height="68" viewBox="0 0 68 68" stroke="var(--nav-grey)" stroke-width="6" stroke-linecap="round">
      <path d="M10 62V46M28 62V30M46 62V12"/>
    </svg>
    <span>Stats</span>
  </div>
  <div class="nav-item" style="left:971px">
    <svg width="68" height="68" viewBox="0 0 68 68" fill="none" stroke="var(--nav-grey)" stroke-width="6" stroke-linecap="round">
      <circle cx="34" cy="20" r="11"/><path d="M12 62c0-14 9-22 22-22s22 8 22 22"/>
    </svg>
    <span>Profile</span>
  </div>
</div>
</body>
</html>
```